Zine template for Velvet Orchard Zine

I wanted to create a zine template in inDesign or but could use some design expertise.  I have attached my draft doc.  the zine will sometimes be 32 pages, or 40 pages (8.5inches x 11, folded in 1/2). the publicaton is photocopied so placing pages in right order is important for easier assembly. I can attach sample.
I am open to masthead improvement (velvet orchard...pages you can touch).  But needs to look more like "hand made" -not too slick.  I am open to changing icon (pen dipping in water making waves...) to something that suggests a tactile, sensory impact.
I will fill in content myself for each edition.  But need page set ups that is column grid based.  So I can play with layout.  But wanted  a core based design that can make sure each edition is coherent.
Title page-same format but of course different theme, main pic, and contents
Letter from Editor/Table of Contents-again, format same, but content will change
Need 1 double page layout with double column layout option
1 double page layout with single column layout option
Maybe one with triple column layout option.
Common page number format-using shoe icon
I like idea of common theme based header or footer on each page
Add bus card info under Brindlewick press
Needs to have at least 1/2 inch margin around edges as it is copied and don't want content to bleed off page.
REmember pages stapled so need enough space between columns in middle to allow for staple and still read content
DOes this make sense?  Essentially looking for a mag layout for zine (which is just using std letter size paper, folder, and stapled to make a zine (like a pamphlet).  I uploaded a few samples of layouts and how the pages work.
Let me know if you have questions!

```html
<!DOCTYPE html>
<html lang="en">
<head>
<meta charset="utf-8">
<title>Velvet Orchard Zine — Cover</title>
<link rel="stylesheet" href="https://fonts.googleapis.com/css2?family=Bebas+Neue&family=Nothing+You+Could+Do&family=Oswald:wght@600&display=swap">
<style>
  :root {
    --ink: #221f20;
    --paper: #ffffff;
    --mist-light: #eef0f1;
    --mist-mid: #c9cdd0;
    --mist-dark: #7f8488;
    --dusk: #2b2b2e;
    --cover-w: 777px;
    --cover-h: 1200px;
  }
  * { margin: 0; padding: 0; box-sizing: border-box; }
  html, body { width: var(--cover-w); height: var(--cover-h); overflow: hidden; background: var(--paper); }
  .cover { position: relative; width: var(--cover-w); height: var(--cover-h); overflow: hidden; background: var(--paper); color: var(--ink); }

  .cover-photo {
    position: absolute; left: 0; top: 560px; width: 100%; height: 640px;
    background: linear-gradient(to bottom, var(--paper) 0%, var(--mist-light) 14%, var(--mist-mid) 45%, var(--mist-dark) 78%, var(--dusk) 100%);
  }

  .masthead-band { position: absolute; left: 0; top: 92px; width: 100%; height: 150px; }
  .masthead-mark {
    position: absolute; left: 50px; top: 140px; width: 46px; height: 46px;
    border-radius: 50%; background: var(--paper);
  }
  .masthead-name {
    position: absolute; left: 150px; top: 108px;
    font-family: "Nothing You Could Do", cursive; font-size: 72px; line-height: 1;
    color: var(--paper); white-space: nowrap;
  }
  .issue-info {
    position: absolute; left: 645px; top: 142px; text-align: center; color: var(--paper);
    font-family: "Oswald", sans-serif; font-weight: 600; line-height: 1.1;
  }
  .issue-info .volume { font-size: 12px; letter-spacing: 0.2px; }
  .issue-info .price { font-size: 19px; }

  .tagline {
    position: absolute; right: 48px; top: 246px;
    font-family: "Nothing You Could Do", cursive; font-size: 34px; color: var(--ink); white-space: nowrap;
  }

  .contents { position: absolute; left: 60px; top: 332px; list-style: none; }
  .contents li {
    font-family: "Bebas Neue", sans-serif; font-size: 44px; line-height: 47px;
    color: var(--ink); letter-spacing: -0.3px;
  }
  .contents .indent { display: block; padding-left: 28px; }

  .doubts {
    position: absolute; left: 70px; top: 700px; transform: rotate(-11deg); transform-origin: left top;
    font-family: "Nothing You Could Do", cursive; font-size: 36px; line-height: 48px; color: var(--ink);
  }
  .doubts span { display: block; white-space: nowrap; }

  .availability {
    position: absolute; left: 0; width: 100%; top: 1114px; text-align: center;
    font-family: "Bebas Neue", sans-serif; font-size: 30px; letter-spacing: 1px; color: var(--paper);
  }
</style>
</head>
<body>
<main class="cover">
  <div class="cover-photo" role="img" aria-label="Misty grey sky over a ridge with the silhouette of a woman standing, a sword resting on her shoulder"></div>

  <svg class="masthead-band" viewBox="0 0 777 150" preserveAspectRatio="none" aria-hidden="true">
    <path fill="#221f20" d="M0 6 L60 2 L130 8 L210 0 L300 5 L380 1 L470 7 L560 2 L650 6 L720 0 L777 4 L777 118 L740 128 L700 122 L660 140 L610 130 L560 146 L500 134 L440 148 L380 136 L320 150 L260 138 L200 146 L140 132 L90 142 L40 130 L0 138 Z"/>
  </svg>
  <div class="masthead-mark" aria-hidden="true"></div>
  <h1 class="masthead-name">Velvet Orchard</h1>
  <div class="issue-info">
    <div class="volume">VOLUME #1, 2014</div>
    <div class="price">$5.00</div>
  </div>

  <p class="tagline">...pages you can touch</p>

  <ul class="contents">
    <li>#Girl-trapreneur Interupted</li>
    <li>#Top Trends</li>
    <li>#Secrets to Success in the<span class="indent">Second Machine Age Economy</span></li>
    <li>#Necessary Endings</li>
    <li>#Cool Resources</li>
  </ul>

  <p class="doubts">
    <span>It s Not Possible</span>
    <span>Too Risky</span>
    <span>But you have no experience</span>
  </p>

  <p class="availability">Not available on line. Hard copy only</p>
</main>
</body>
</html>
```